Geschäftsunterlagen mit vorhandenem Logo
Zielgruppe
- Immobilienmakler.
- Vermietung und Verkauf von Immobilien
- Eigentümer, Bauträger, Hausverwaltungen, Immobilienentwickler, Wohnungsbaugesellschaften, Käufer und Mieter.
Aufgabenstellung
Wir suchen ein neues Design für unsere Geschäftsunterlagen. Es soll dem Betrachter ein gutes Gefühl vermittelt. Es soll seriös, edel und dynamisch wirken, aber auch vertrauensvoll und kompetent.
Wir suchen neue Designs für folgende Unterlagen, das Logo soll hierbei etwas stärker im Vordergrund stehen :
- Visitenkarten ( Text= Logo, mein Name Jonas Weidler, Handynr. und Webseite )
- Briefpapier ( Text= Logo, Firmenname, Adresse, email, Tel-Nr., event. Bankverbindung ) + Briefumschlag ( Din-Lang ) + email-Vorlage ( Logo + Firmenname, Adresse + Telefon )
- Mappe für Unterlagen ( Din A4 )
- Vermietungsschild und Verkaufsschild fürs Objekt ( 1. H=700mm x B=440mm und 2. H=600 x B 1000mm ) Falls die Schilder zu viel sind, lassen Sie die Entwürfe bitte weg. Priorität haben die anderen Unterlagen.
Logo ist vorhanden, die Schrift kann noch variiert werden.
Falls Sie Fragen haben, schreiben Sie uns bitte an.

```html
<!DOCTYPE html>
<html lang="de">
<head>
<meta charset="utf-8">
<title>Weidler Immobilien – Geschäftsausstattung</title>
<link href="https://fonts.googleapis.com/css2?family=Open+Sans:wght@400;600&display=swap" rel="stylesheet">
<style>
:root{
  --stage:#adadad;
  --paper:#ffffff;
  --navy:#1f3566;
  --blue:#2f62a8;
  --sky:#6cc4f4;
  --ink:#1d1d1d;
  --accent:#3d7cc4;
  --faint:#f6f6f6;
  --window:#f1f1f1;
}
*{margin:0;padding:0;box-sizing:border-box}
html,body{width:1200px;height:838px;overflow:hidden;background:var(--stage);font-family:"Open Sans",sans-serif;color:var(--ink)}
.piece{position:absolute;background:var(--paper);overflow:hidden}
.mark{position:absolute;border-radius:50%;background:var(--blue)}
.wordmark{position:absolute;font-weight:400;letter-spacing:.12em;line-height:1;color:var(--ink)}
.wordmark span{display:block}
.wordmark .sub{letter-spacing:.22em}
.faint-disc{position:absolute;border-radius:50%;background:var(--faint)}
.band{position:absolute;left:0;right:0;bottom:0;background:var(--navy)}
.tab{position:absolute;right:0;background:linear-gradient(90deg,var(--navy),var(--blue) 60%,var(--accent));border-left:1.5px solid #fff;border-bottom:1.5px solid #fff;border-bottom-left-radius:12px;color:#fff;text-align:center}

/* Letterhead */
.letterhead{left:36.6px;top:40.8px;width:525.7px;height:744px}
.letterhead .topline{position:absolute;left:0;right:0;top:0;height:3.5px;background:linear-gradient(90deg,var(--navy),var(--sky) 50%,var(--navy))}
.letterhead .mark{left:229px;top:37px;width:38px;height:38px}
.letterhead .wordmark{left:281px;top:43px;font-size:21px}
.letterhead .wordmark .sub{font-size:11.5px;margin-top:3px}
.letterhead .divider{position:absolute;left:404px;top:31px;width:1px;height:50px;background:#555}
.contact{position:absolute;left:410px;top:29px;font-size:7.4px;line-height:10px}
.contact .gap{height:3.5px}
.contact svg{width:6px;height:6px;vertical-align:-1px;margin-right:4px;fill:var(--accent)}
.contact .mail{font-size:8.3px}
.sender{position:absolute;left:51px;top:129px;font-size:4.6px;border-bottom:.6px solid #333;padding-bottom:1px}
.letterhead .faint-disc{left:97px;top:262px;width:344px;height:356px}
.legal{position:absolute;top:707px;font-size:7.4px;line-height:10px;color:#333}
.legal.col1{left:37px}.legal.col2{left:158px}.legal.col3{left:239px}
.legal-rule{position:absolute;top:706px;width:.8px;height:22px;background:#555}
.letterhead .band{height:13px}
.letterhead .tab{left:376px;top:723px;height:14px;font-size:8px;line-height:12px}

/* Business card front */
.card{width:222.6px;height:127px;border-radius:10px;top:48px}
.card-front{left:641.7px}
.card-front .mark{left:70px;top:18px;width:32px;height:32px}
.card-front .wordmark{left:113px;top:23px;font-size:16.5px}
.card-front .wordmark .sub{font-size:8.4px;margin-top:2px}
.holder{position:absolute;left:14px;top:69px;font-size:8.8px;color:var(--accent)}
.role{position:absolute;left:14px;top:81px;font-size:5.4px}
.card-lines{position:absolute;left:14px;top:98px;font-size:5.4px;line-height:8px}
.card-lines svg{width:4.5px;height:4.5px;fill:var(--accent);margin-right:4px;vertical-align:-.5px}
.card-front .band{height:8px}
.card-front .tab{left:134px;top:114px;height:9px;font-size:5.2px;line-height:8px;border-bottom-left-radius:8px}

/* Business card back */
.card-back{left:905.2px;background:radial-gradient(circle at 75% 45%,var(--sky) 0%,var(--blue) 45%,var(--navy) 100%)}
.card-back .mark{left:135px;top:16px;width:40px;height:40px;background:none;border:3px solid #fff}
.card-back .wordmark{left:0;right:0;top:62px;text-align:center;color:#fff;font-size:17px;padding-left:78px}
.card-back .wordmark .sub{font-size:9.2px;margin-top:2px}
.card-back .web{position:absolute;left:78px;right:0;top:105px;text-align:center;color:#fff;font-size:5.6px;letter-spacing:.08em}

/* Envelope back */
.envelope-back{left:606.2px;top:205.4px;width:551.3px;height:275.4px}
.flap{position:absolute;left:0;top:0}
.envelope-back .mark{left:251px;top:15px;width:50px;height:50px;background:none;border:3.5px solid #fff}
.return{position:absolute;left:0;right:0;top:247px;text-align:center;font-size:7.4px}
.return b{font-weight:400;color:var(--accent)}

/* Envelope front */
.envelope-front{left:606.2px;top:509.5px;width:551.3px;height:275.4px}
.envelope-front .faint-disc{left:334px;top:-6px;width:216px;height:214px}
.envelope-front .mark{left:63px;top:45px;width:42px;height:42px}
.envelope-front .wordmark{left:119px;top:53px;font-size:22px}
.envelope-front .wordmark .sub{font-size:11.6px;margin-top:3px}
.address-window{position:absolute;left:62.7px;top:121px;width:225.3px;height:112px;background:var(--window);border:1px solid #c9c9c9;border-radius:12px}
.envelope-front .band{height:13px}
.envelope-front .tab{left:401px;top:256px;height:14px;font-size:8px;line-height:12px}
</style>
</head>
<body>

<section class="piece letterhead" aria-label="Briefpapier">
  <div class="topline"></div>
  <div class="mark"></div>
  <div class="wordmark"><span>WEIDLER</span><span class="sub">IMMOBILIEN</span></div>
  <div class="divider"></div>
  <div class="contact">
    Lindenauer Straße 14<br>10785 Berlin
    <div class="gap"></div>
    <svg viewBox="0 0 10 10"><path d="M2 1l2 2-1 1.5c.6 1.2 1.3 1.9 2.5 2.5L7 6l2 2-1.5 1.5C4 9 1 6 .5 2.5z"/></svg>0261 - 48 71 0 20<br>
    <svg viewBox="0 0 10 10"><rect x="2.5" y="0" width="5" height="3"/><rect x="0" y="3.5" width="10" height="4"/><rect x="2.5" y="7" width="5" height="3"/></svg>0261 - 48 71 0 21<br>
    <span class="mail"><svg viewBox="0 0 10 10"><path d="M0 2h10v6H0z M0 2l5 3.5L10 2" stroke="#fff" stroke-width=".7"/></svg>info@weidler-immo.de</span>
  </div>
  <div class="sender">WEIDLER IMMOBILIEN | Lindenauer Straße 14 | 10785 Berlin</div>
  <div class="faint-disc"></div>
  <div class="legal col1">Steuerliche ID: De418930500<br>Umsatzsteuer ID: 37 000 621 000</div>
  <div class="legal-rule" style="left:150px"></div>
  <div class="legal col2">Bankwerbindung:<br>Stadtbank Berlin</div>
  <div class="legal-rule" style="left:231px"></div>
  <div class="legal col3">BIC: STBADEBB000<br>IBAN: DE41 3872 0091 0450 0000 62</div>
  <div class="band"></div>
  <div class="tab">www.weidler-immo.de</div>
</section>

<section class="piece card card-front" aria-label="Visitenkarte Vorderseite">
  <div class="mark"></div>
  <div class="wordmark"><span>WEIDLER</span><span class="sub">IMMOBILIEN</span></div>
  <div class="holder">Jonas Weidler</div>
  <div class="role">Geschäftsführer</div>
  <div class="card-lines">
    <svg viewBox="0 0 10 10"><rect x="2" y="0" width="6" height="10" rx="1"/></svg>0176- 512 83 470<br>
    <svg viewBox="0 0 10 10"><path d="M0 2h10v6H0z"/></svg>weidler@weidler-immo.de
  </div>
  <div class="band"></div>
  <div class="tab">www.weidler-immo.de</div>
</section>

<section class="piece card card-back" aria-label="Visitenkarte Rückseite">
  <div class="mark"></div>
  <div class="wordmark"><span>WEIDLER</span><span class="sub">IMMOBILIEN</span></div>
  <div class="web">www.weidler-immo.de</div>
</section>

<section class="piece envelope-back" aria-label="Briefumschlag Rückseite">
  <svg class="flap" width="551.3" height="83" viewBox="0 0 551.3 83">
    <defs>
      <linearGradient id="flapGradient" x1="0" x2="1" y1="0" y2="0">
        <stop offset="0" stop-color="#1f3566"/>
        <stop offset=".5" stop-color="#6cc4f4"/>
        <stop offset="1" stop-color="#1f3566"/>
      </linearGradient>
    </defs>
    <path d="M0 0H551.3L532 70Q528.5 82 516 82H35Q24 82 20.5 70Z" fill="url(#flapGradient)"/>
  </svg>
  <div class="mark"></div>
  <div class="return">WEIDLER IMMOBILIEN <b>|</b> Lindenauer Straße 14 <b>|</b> 10785 Berlin</div>
</section>

<section class="piece envelope-front" aria-label="Briefumschlag Vorderseite">
  <div class="faint-disc"></div>
  <div class="mark"></div>
  <div class="wordmark"><span>WEIDLER</span><span class="sub">IMMOBILIEN</span></div>
  <div class="address-window"></div>
  <div class="band"></div>
  <div class="tab">www.weidler-immo.de</div>
</section>

</body>
</html>
```